Lakeshore Claim Advocates Business card

We need to get business card Design for our Company we are Public Adjusters in Chicago Illinois - i like to see good combination and elements from my Company Logo. as well To be an two side design

Target Market(s)

Home /Business owner Property Managers

Industry/Entity Type

Business

Contact Information for Business Card

to show the Element of our logo i will Like 3D

Font styles to use
Sans Serif

Requirements
Must have
• Logo and Element of the Logo in 3D
Nice to have
• Logo That we Provide 3D Same Colors or open for suggestions
Should not have
• unleare view -

```html
<!DOCTYPE html>
<html lang="en">
<head>
<meta charset="utf-8">
<title>Lakeshore Claim Advocates – Business Card</title>
<link rel="stylesheet" href="https://fonts.googleapis.com/css2?family=Open+Sans:wght@400;600;700&display=swap">
<style>
  :root {
    --backdrop: #2b2b2d;
    --card-white: #ffffff;
    --brand-blue: #2a45a8;
    --brand-blue-deep: #1f3893;
    --ink-navy: #28338f;
    --link-blue: #4a63b8;
    --panel-text: #ffffff;
    --panel-soft: #c9d3f2;
    --card-shadow: 0 18px 40px rgba(0, 0, 0, 0.45);
  }
  * { box-sizing: border-box; margin: 0; padding: 0; }
  html, body {
    width: 1200px;
    height: 1000px;
    overflow: hidden;
    background: var(--backdrop);
    font-family: "Open Sans", Arial, sans-serif;
  }
  .stage { position: relative; width: 1200px; height: 1000px; }

  .card {
    position: absolute;
    width: 640px;
    height: 366px;
    background: var(--card-white);
    border-radius: 34px;
    box-shadow: var(--card-shadow);
    overflow: hidden;
  }
  .card--front { left: 110px; top: 90px; }
  .card--back  { left: 450px; top: 540px; }

  .brand {
    position: absolute;
    display: flex;
    flex-direction: column;
    align-items: center;
    text-align: center;
  }
  .brand__dot {
    width: 64px;
    height: 64px;
    border-radius: 50%;
    background: var(--brand-blue);
    margin-bottom: 18px;
  }
  .brand__name {
    color: var(--ink-navy);
    font-weight: 700;
    font-size: 25px;
    line-height: 1.15;
  }
  .card--front .brand { left: 0; right: 0; top: 78px; }
  .card--back .brand { left: 24px; width: 260px; top: 100px; }
  .card--back .brand__name { font-size: 22px; }

  .web-line {
    position: absolute;
    left: 0; right: 0; top: 270px;
    display: flex;
    justify-content: center;
    align-items: center;
    gap: 8px;
    color: var(--link-blue);
    font-size: 15px;
  }
  .web-line svg { width: 14px; height: 14px; }

  .contact-panel {
    position: absolute;
    top: 0; right: 0; bottom: 0;
    width: 336px;
    background: linear-gradient(135deg, var(--brand-blue), var(--brand-blue-deep));
    clip-path: polygon(0 0, 100% 0, 100% 100%, 0 100%, 0 44%, 14px 40%, 0 36%);
    padding: 86px 24px 0 44px;
    color: var(--panel-text);
  }
  .contact-panel__name { font-size: 22px; font-weight: 700; line-height: 1.2; }
  .contact-panel__role { font-size: 15px; margin-bottom: 10px; }
  .contact-panel__address { font-size: 14px; color: var(--panel-soft); line-height: 1.4; margin-bottom: 12px; }
  .contact-list { list-style: none; }
  .contact-list li {
    display: flex;
    align-items: center;
    gap: 10px;
    font-size: 13.5px;
    color: var(--panel-soft);
    line-height: 1.6;
    white-space: nowrap;
  }
  .contact-list svg { width: 12px; height: 12px; flex: none; fill: var(--panel-text); }
  .contact-list strong { color: var(--panel-text); font-weight: 600; }
</style>
</head>
<body>
<main class="stage">

  <section class="card card--front" aria-label="Business card front">
    <div class="brand">
      <span class="brand__dot"></span>
      <p class="brand__name">Lakeshore Claim Advocates</p>
    </div>
    <p class="web-line">
      <svg viewBox="0 0 16 16" aria-hidden="true"><circle cx="8" cy="8" r="7" fill="#4a63b8"/><path d="M1 8h14M8 1c-3 3.5-3 10.5 0 14M8 1c3 3.5 3 10.5 0 14" stroke="#fff" stroke-width="1" fill="none"/></svg>
      <span>www.lakeshoreclaims.example</span>
    </p>
  </section>

  <section class="card card--back" aria-label="Business card back">
    <div class="brand">
      <span class="brand__dot"></span>
      <p class="brand__name">Lakeshore Claim<br>Advocates</p>
    </div>
    <div class="contact-panel">
      <p class="contact-panel__name">Daniel Reyes</p>
      <p class="contact-panel__role">Director</p>
      <p class="contact-panel__address">Your Street Address<br>Chicago, IL 1234</p>
      <ul class="contact-list">
        <li><svg viewBox="0 0 16 16" aria-hidden="true"><path d="M3 1l3 3-2 2c1 2 3 4 5 5l2-2 3 3-2 3C6 15 1 10 0 3z"/></svg><span>+000 12345 6789</span></li>
        <li><svg viewBox="0 0 16 16" aria-hidden="true"><path d="M0 3h16v10H0zM1 4l7 5 7-5" stroke="#2a45a8" stroke-width="1"/></svg><span>dreyes@lakeshoreclaims.example</span></li>
        <li><svg viewBox="0 0 16 16" aria-hidden="true"><circle cx="8" cy="8" r="7.5"/><path d="M1 8h14M8 1c-3 3.5-3 10.5 0 14M8 1c3 3.5 3 10.5 0 14" stroke="#2a45a8" stroke-width="1" fill="none"/></svg><span>www.<strong>lakeshoreclaims.example</strong></span></li>
      </ul>
    </div>
  </section>

</main>
</body>
</html>
```